Sales Training Power Point Presentation

We are looking for a power point presentation that allows us to turn our training manual into a presentation. I am attaching the training manual here, just to give an idea of what we will be presenting. We want to be able to have graphs for some of that data and be able to move around slides/edit as we see it is needed.

Target Market(s)

new sales employees

Industry/Entity Type

staffing

Colors
0054AA
0677BA
7BADD7
CADEEF
E8F1F8
F0912C
F2A743
F7CA91
FBE8D2
FDF5EE

Requirements
Must have
• graphs

```html
<!DOCTYPE html>
<html lang="en">
<head>
<meta charset="utf-8">
<title>Kestrel Group – Sales Training Deck</title>
<link href="https://fonts.googleapis.com/css2?family=Montserrat:wght@400;500;600;700&family=Open+Sans:wght@400;600&display=swap" rel="stylesheet">
<style>
:root{
  --navy:#2e3d50;
  --navy-2:#3d4e64;
  --orange:#F0912C;
  --orange-2:#F2A743;
  --peach:#F7CA91;
  --cream:#FBE8D2;
  --blue:#0677BA;
  --sky:#7BADD7;
  --ice:#E8F1F8;
  --ink:#3a3f46;
  --muted:#7d8590;
  --rule:#d9dde2;
  --page:#eceef1;
  --photo-a:#cfc8bf;
  --photo-b:#8e8b88;
}
*{box-sizing:border-box;margin:0;padding:0}
html,body{width:1200px;height:2400px;overflow:hidden;background:var(--page)}
body{font-family:"Open Sans",Arial,sans-serif;color:var(--ink)}
.canvas{position:relative;width:1200px;height:2400px;overflow:hidden}

.slide{position:absolute;width:525px;height:255px;background:#fff;overflow:hidden;box-shadow:0 2px 8px rgba(30,40,55,.12)}
.col-l{left:60px}.col-r{left:615px}
.r1{top:420px}.r2{top:700px}.r3{top:980px}.r4{top:1260px}.r5{top:1540px}.r6{top:1820px}.r7{top:2100px}

.abs{position:absolute}
.photo{position:absolute;background:linear-gradient(135deg,var(--photo-a),var(--photo-b))}
.photo.warm{background:linear-gradient(135deg,#d9cfc4,#9c8e80)}
.photo.cool{background:linear-gradient(135deg,#c7ccd2,#7f8893)}

.brand{position:absolute;display:flex;align-items:center;gap:5px;font-family:"Montserrat",sans-serif;font-weight:700;letter-spacing:.08em;color:var(--navy);font-size:7px;white-space:nowrap}
.brand .dot{width:10px;height:10px;border-radius:50%;background:var(--orange)}
.brand.light{color:#fff}
.brand.big{font-size:12px;gap:8px}
.brand.big .dot{width:20px;height:20px}

.kicker{font-family:"Montserrat",sans-serif;font-weight:600;font-size:9px;color:var(--orange);letter-spacing:.06em;text-transform:uppercase}
.title{font-family:"Montserrat",sans-serif;font-weight:700;font-size:17px;color:var(--navy);text-transform:uppercase;line-height:1.05}
.title.light{color:#fff}
.body{font-size:7px;line-height:1.45;color:var(--muted)}
.body.light{color:#d5dbe3}
.foot{position:absolute;left:0;right:0;bottom:0;height:6px;background:var(--navy)}
.foot::after{content:"";position:absolute;right:0;top:0;width:38%;height:6px;background:var(--orange)}

.pill{display:inline-block;background:var(--orange);color:#fff;font-family:"Montserrat",sans-serif;font-weight:600;font-size:9px;padding:3px 12px;border-radius:2px}

/* cover */
.cover{position:absolute;left:60px;top:30px;width:1080px;height:360px;background:#fff;overflow:hidden;box-shadow:0 3px 12px rgba(30,40,55,.14)}
.cover .headline{position:absolute;left:70px;top:150px;font-family:"Montserrat",sans-serif;font-weight:500;font-size:54px;color:var(--orange);letter-spacing:.02em}
.cover .date{position:absolute;left:70px;top:268px;font-family:"Montserrat",sans-serif;font-size:15px;color:var(--navy)}

/* toc */
.toc-list{list-style:none;position:absolute;left:24px;top:92px;width:190px}
.toc-list li{font-family:"Montserrat",sans-serif;font-size:7px;font-weight:600;color:var(--navy);padding:5px 0;border-bottom:1px solid var(--rule);display:flex;justify-content:space-between}
.toc-list li span{color:var(--orange)}

.icon-row{position:absolute;left:0;right:0;bottom:6px;height:40px;background:var(--navy);display:flex;justify-content:space-around;align-items:center}
.icon-row .ic{width:18px;height:18px;border-radius:50%;border:2px solid var(--orange)}

.cap{font-size:6.5px;line-height:1.4;color:var(--muted)}
.cap b{display:block;color:var(--navy);font-family:"Montserrat",sans-serif;font-size:7.5px;margin-bottom:2px}

table.compare{position:absolute;left:200px;top:40px;width:300px;border-collapse:collapse;font-size:6.5px}
table.compare th{font-family:"Montserrat",sans-serif;font-size:8px;color:#fff;padding:5px;text-align:center}
table.compare th.contract{background:var(--orange)}
table.compare th.fulltime{background:var(--navy)}
table.compare td{padding:5px 6px;border-bottom:1px solid var(--rule);color:var(--muted);text-align:center}
table.compare tr:nth-child(even) td{background:#f6f7f9}

.vp-list{list-style:none;position:absolute;left:290px;top:78px;width:210px}
.vp-list li{display:flex;align-items:center;gap:8px;font-size:7px;color:var(--navy);font-weight:600;margin-bottom:11px}
.vp-list li i{width:16px;height:16px;border-radius:50%;background:var(--orange);flex:none}

.pillars{position:absolute;left:20px;right:20px;top:84px;display:flex;gap:8px}
.pillar{flex:1;text-align:center}
.pillar .ic{width:30px;height:30px;border-radius:50%;border:2px solid var(--orange);margin:0 auto 6px}
.pillar b{display:block;font-family:"Montserrat",sans-serif;font-size:7.5px;color:var(--navy);margin-bottom:3px}
.pillar p{font-size:6px;line-height:1.4;color:var(--muted)}
.pillars-band{position:absolute;left:0;right:0;top:72px;height:2px;background:var(--orange)}

.tiles{position:absolute;left:24px;top:70px;width:300px;display:grid;grid-template-columns:repeat(3,1fr);gap:6px}
.tile{height:72px;position:relative;background:var(--orange);color:#fff;font-family:"Montserrat",sans-serif;font-size:7px;font-weight:600;display:flex;align-items:center;justify-content:center;text-align:center;padding:6px}
.tile.navy{background:var(--navy)}
.tile.photo-tile{background:linear-gradient(135deg,var(--photo-a),var(--photo-b))}
</style>
</head>
<body>
<div class="canvas">

  <!-- Cover -->
  <section class="cover">
    <svg class="abs" style="left:0;top:0" width="1080" height="360" viewBox="0 0 1080 360">
      <polygon points="0,0 520,0 470,40 0,40" fill="#2e3d50"/>
      <polygon points="520,0 560,0 510,40 470,40" fill="#F0912C"/>
    </svg>
    <div class="photo warm" style="left:520px;top:0;width:560px;height:360px;clip-path:polygon(18% 0,100% 0,100% 100%,0 100%)" role="img" aria-label="Photo of a smiling businesswoman in an office"></div>
    <svg class="abs" style="left:500px;top:0" width="140" height="360" viewBox="0 0 140 360">
      <polygon points="100,0 124,0 24,360 0,360" fill="#F0912C"/>
    </svg>
    <div class="brand big" style="left:70px;top:68px"><span class="dot"></span>KESTREL GROUP</div>
    <div class="headline">SALES TRAINING</div>
    <div class="abs" style="left:70px;top:225px;width:300px;height:2px;background:var(--orange)"></div>
    <div class="date">July 2023</div>
  </section>

  <!-- Row 1 -->
  <section class="slide col-l r1">
    <div class="photo warm" style="left:250px;top:0;width:275px;height:249px;clip-path:polygon(20% 0,100% 0,100% 100%,0 100%)" role="img" aria-label="Photo of a businesswoman smiling"></div>
    <svg class="abs" style="left:0;top:0" width="525" height="255"><polygon points="0,0 70,0 0,40" fill="#2e3d50"/><polygon points="250,249 300,0 312,0 262,249" fill="#F0912C"/></svg>
    <div class="brand" style="left:26px;top:50px"><span class="dot"></span>KESTREL GROUP</div>
    <div class="abs" style="left:26px;top:90px;font-family:'Montserrat',sans-serif;font-weight:500;font-size:26px;color:var(--orange);line-height:1">SALES<br>TRAINING</div>
    <div class="abs" style="left:26px;top:160px"><span class="pill">July 2023</span></div>
    <div class="foot"></div>
  </section>

  <section class="slide col-r r1" style="background:var(--navy)">
    <div class="photo warm" style="left:240px;top:0;width:285px;height:249px;clip-path:polygon(16% 0,100% 0,100% 100%,0 100%)" role="img" aria-label="Photo of a businesswoman smiling"></div>
    <svg class="abs" style="left:0;top:0" width="525" height="255"><polygon points="240,249 286,0 298,0 252,249" fill="#F0912C"/></svg>
    <div class="brand light" style="left:26px;top:50px"><span class="dot"></span>KESTREL GROUP</div>
    <div class="abs" style="left:26px;top:90px;font-family:'Montserrat',sans-serif;font-weight:500;font-size:26px;color:#fff;line-height:1">SALES<br>TRAINING</div>
    <div class="abs" style="left:26px;top:160px"><span class="pill">July 2023</span></div>
    <div class="foot" style="background:var(--orange)"></div>
  </section>

  <!-- Row 2 -->
  <section class="slide col-l r2">
    <div class="abs" style="left:24px;top:24px"><div class="kicker">Table</div><div class="title">Of Contents</div></div>
    <ul class="toc-list">
      <li>Industry Acumen<span>01</span></li>
      <li>Kestrel's Value Proposition<span>02</span></li>
      <li>Sales Cycle<span>03</span></li>
      <li>Account Penetration<span>04</span></li>
      <li>Systems &amp; Tools<span>05</span></li>
      <li>Business Growth<span>06</span></li>
    </ul>
    <div class="photo" style="left:280px;top:0;width:245px;height:249px;clip-path:polygon(22% 0,100% 0,100% 100%,0 100%)" role="img" aria-label="Photo of colleagues reviewing documents"></div>
    <svg class="abs" style="left:0;top:0" width="525" height="255"><polygon points="434,0 525,0 525,70" fill="#2e3d50"/></svg>
    <div class="foot"></div>
  </section>

  <section class="slide col-r r2">
    <div class="brand" style="right:18px;top:14px"><span class="dot"></span>KESTREL GROUP</div>
    <div class="abs" style="left:24px;top:24px"><div class="kicker">Staffing</div><div class="title" style="font-size:14px">And Recruiting Industry</div></div>
    <p class="body abs" style="left:24px;top:72px;width:250px">The staffing market keeps growing year after year. Firms rely on flexible talent to meet demand, and our team helps clients find the right people fast. <b style="color:var(--orange)">Over 16 million</b> workers are placed by agencies each year, across light industrial, office, tech and health care roles.</p>
    <svg class="abs" style="left:330px;top:48px" width="160" height="150" viewBox="0 0 160 150" role="img" aria-label="Pie chart of staffing market share by sector">
      <g transform="translate(70,72) rotate(-90)">
        <circle r="25" fill="none" stroke="#F0912C" stroke-width="50" stroke-dasharray="70.7 157.1"/>
        <circle r="25" fill="none" stroke="#aab2bc" stroke-width="50" stroke-dasharray="39.3 157.1" stroke-dashoffset="-70.7"/>
        <circle r="25" fill="none" stroke="#2e3d50" stroke-width="50" stroke-dasharray="31.4 157.1" stroke-dashoffset="-110"/>
        <circle r="25" fill="none" stroke="#F7CA91" stroke-width="50" stroke-dasharray="15.7 157.1" stroke-dashoffset="-141.4"/>
      </g>
      <text x="96" y="60" font-size="8" font-family="Montserrat" font-weight="700" fill="#fff">45%</text>
      <text x="30" y="102" font-size="8" font-family="Montserrat" font-weight="700" fill="#fff">25%</text>
      <text x="30" y="55" font-size="8" font-family="Montserrat" font-weight="700" fill="#fff">20%</text>
    </svg>
    <div class="icon-row"><span class="ic"></span><span class="ic"></span><span class="ic"></span><span class="ic"></span><span class="ic"></span></div>
  </section>

  <!-- Row 3 -->
  <section class="slide col-l r3">
    <div class="abs" style="left:0;top:0;width:180px;height:255px;background:var(--navy)"></div>
    <div class="abs" style="left:20px;top:24px"><div class="kicker">Industry</div><div class="title light">Acumen:</div></div>
    <p class="body light abs" style="left:20px;top:78px;width:145px">Know the market you sell into. Learn the terms, the trends and the roles our clients hire for most. Strong industry acumen builds trust with every buyer and sets you apart from other agencies.</p>
    <p class="body abs" style="left:200px;top:26px;width:300px">Key facts for new sales staff: staffing firms place temporary, contract and full-time workers for clients in many sectors.</p>
    <div class="photo" style="left:200px;top:70px;width:145px;height:120px" role="img" aria-label="Photo of a team meeting around a table"></div>
    <div class="photo cool" style="left:355px;top:70px;width:145px;height:120px" role="img" aria-label="Photo of a recruiter talking with a candidate"></div>
    <div class="brand" style="right:18px;bottom:18px"><span class="dot"></span>KESTREL GROUP</div>
    <div class="foot"></div>
  </section>

  <section class="slide col-r r3">
    <div class="abs" style="left:0;top:0;width:525px;height:50px;background:var(--navy)"></div>
    <div class="abs" style="left:0;top:50px;width:525px;height:3px;background:var(--orange)"></div>
    <div class="title light abs" style="left:0;right:0;top:16px;text-align:center">Staffing Arrangements</div>
    <div class="photo" style="left:24px;top:70px;width:150px;height:90px" role="img" aria-label="Photo of a temporary worker on site"></div>
    <div class="photo cool" style="left:187px;top:70px;width:150px;height:90px" role="img" aria-label="Photo of a contract professional at a desk"></div>
    <div class="photo warm" style="left:350px;top:70px;width:150px;height:90px" role="img" aria-label="Photo of a new full-time hire shaking hands"></div>
    <p class="cap abs" style="left:24px;top:170px;width:150px"><b>Temporary</b>Short term help for peak load, leave cover or one-off projects.</p>
    <p class="cap abs" style="left:187px;top:170px;width:150px"><b>Contract to Hire</b>Trial period first, then the client may hire the worker full time.</p>
    <p class="cap abs" style="left:350px;top:170px;width:150px"><b>Direct Hire</b>We recruit and screen; the client hires the person directly.</p>
    <div class="foot"></div>
  </section>

  <!-- Row 4 -->
  <section class="slide col-l r4">
    <div class="abs" style="left:24px;top:24px"><div class="kicker">Full-time</div><div class="title">Staffing</div></div>
    <p class="body abs" style="left:24px;top:72px;width:150px">Compare the two main models so you can guide each client to the right fit for their budget and goals.</p>
    <table class="compare">
      <tr><th class="contract">Contract Staffing</th><th class="fulltime">Full-time Staffing</th></tr>
      <tr><td>Flexible length</td><td>Long term role</td></tr>
      <tr><td>Hourly bill rate</td><td>One-time fee</td></tr>
      <tr><td>Fast start</td><td>Full search process</td></tr>
      <tr><td>Worker on our payroll</td><td>Worker on client payroll</td></tr>
      <tr><td>Easy to scale</td><td>Builds core team</td></tr>
    </table>
    <div class="brand" style="right:18px;top:14px"><span class="dot"></span>KESTREL GROUP</div>
    <div class="foot"></div>
  </section>

  <section class="slide col-r r4">
    <div class="brand" style="right:18px;top:14px"><span class="dot"></span>KESTREL GROUP</div>
    <div class="abs" style="left:24px;top:24px"><div class="kicker">Kestrel</div><div class="title">Value Proposition</div></div>
    <div class="photo" style="left:24px;top:78px;width:120px;height:75px" role="img" aria-label="Photo of a sales meeting"></div>
    <div class="photo cool" style="left:150px;top:78px;width:120px;height:75px" role="img" aria-label="Photo of a recruiter on a call"></div>
    <div class="photo warm" style="left:24px;top:159px;width:246px;height:70px" role="img" aria-label="Photo of a team in an office"></div>
    <ul class="vp-list">
      <li><i></i>We deliver qualified talent quickly</li>
      <li><i></i>We know your local job market</li>
      <li><i></i>We handle payroll and compliance</li>
      <li><i></i>We stand behind every placement</li>
    </ul>
    <div class="foot"></div>
  </section>

  <!-- Row 5 -->
  <section class="slide col-l r5">
    <div class="brand" style="right:18px;top:14px"><span class="dot"></span>KESTREL GROUP</div>
    <div class="abs" style="left:24px;top:24px"><div class="kicker">Value Proposition</div><div class="title">Kestrel's Value Proposition</div></div>
    <div class="pillars-band"></div>
    <div class="pillars">
      <div class="pillar"><div class="ic"></div><b>Speed</b><p>Roles filled in days, not weeks.</p></div>
      <div class="pillar"><div class="ic"></div><b>Expertise</b><p>Recruiters who know each trade.</p></div>
      <div class="pillar"><div class="ic"></div><b>Specialized Recruiting</b><p>Deep pools of screened talent.</p></div>
      <div class="pillar"><div class="ic"></div><b>Quality</b><p>Checks on skills and fit.</p></div>
      <div class="pillar"><div class="ic"></div><b>Strategic Partnership</b><p>Long term plans with clients.</p></div>
    </div>
    <div class="foot"></div>
  </section>

  <section class="slide col-r r5">
    <div class="brand" style="right:18px;top:14px"><span class="dot"></span>KESTREL GROUP</div>
    <div class="abs" style="left:24px;top:24px"><div class="kicker">The Sales</div><div class="title">Cycle<br>Company</div></div>
    <p class="body abs" style="left:24px;top:80px;width:180px">Every deal moves through six steps. Know where each prospect sits so you can plan the next call, follow up on time and close more business.</p>
    <svg class="abs" style="left:250px;top:30px" width="260" height="210" viewBox="0 0 260 210" role="img" aria-label="Circular diagram of the six-step sales cycle">
      <g transform="translate(130,105) rotate(-90)">
        <circle r="58" fill="none" stroke="#2e3d50" stroke-width="30" stroke-dasharray="57.7 63.8"/>
        <circle r="58" fill="none" stroke="#F0912C" stroke-width="30" stroke-dasharray="57.7 63.8" stroke-dashoffset="-60.7"/>
      </g>
      <circle cx="130" cy="105" r="30" fill="#fff" stroke="#d9dde2"/>
      <text x="130" y="103" text-anchor="middle" font-family="Montserrat" font-weight="700" font-size="8" fill="#2e3d50">SALES</text>
      <text x="130" y="113" text-anchor="middle" font-family="Montserrat" font-weight="700" font-size="8" fill="#2e3d50">CYCLE</text>
      <g font-family="Montserrat" font-size="7" fill="#3a3f46">
        <text x="130" y="10" text-anchor="middle">Prospect</text>
        <text x="220" y="55">Contact</text>
        <text x="220" y="160">Qualify</text>
        <text x="130" y="206" text-anchor="middle">Present</text>
        <text x="40" y="160" text-anchor="end">Close</text>
        <text x="40" y="55" text-anchor="end">Serve</text>
      </g>
    </svg>
    <div class="foot"></div>
  </section>

  <!-- Row 6 -->
  <section class="slide col-l r6">
    <div class="brand" style="right:18px;top:14px"><span class="dot"></span>KESTREL GROUP</div>
    <div class="abs" style="left:24px;top:24px"><div class="kicker">Module 4</div><div class="title">Account Penetration</div></div>
    <p class="body abs" style="left:24px;top:56px;width:320px">Grow each account once you are in. Focus on these steps:</p>
    <div class="tiles">
      <div class="tile">Find New Contacts</div>
      <div class="tile photo-tile" role="img" aria-label="Photo of a handshake"></div>
      <div class="tile navy">Map Hiring Needs</div>
      <div class="tile photo-tile" role="img" aria-label="Photo of a team discussion"></div>
      <div class="tile navy">Business Reviews</div>
      <div class="tile">Expand Services</div>
    </div>
    <p class="body abs" style="left:345px;top:80px;width:155px">Meet each department head, learn their plans and offer help before they ask. Regular reviews keep us top of mind.</p>
    <div class="foot"></div>
  </section>

  <section class="slide col-r r6">
    <div class="brand" style="right:18px;top:14px"><span class="dot"></span>KESTREL GROUP</div>
    <div class="abs" style="left:24px;top:24px"><div class="kicker">Module 5</div><div class="title">Systems<br>Tools</div></div>
    <p class="body abs" style="left:24px;top:80px;width:170px">Our CRM and applicant system hold every lead, contact and job order. Log each call, set tasks and track your pipeline daily so nothing slips through.</p>
    <div class="abs" style="left:220px;top:50px;width:280px;height:170px;border:1px solid var(--rule);background:#f6f8fa">
      <div style="height:14px;background:var(--blue)"></div>
      <div style="position:absolute;left:0;top:14px;width:50px;bottom:0;background:var(--ice)"></div>
      <div style="position:absolute;left:60px;right:10px;top:26px;height:8px;background:#dfe4ea"></div>
      <div style="position:absolute;left:60px;right:10px;top:42px;height:6px;background:#e8ecf0"></div>
      <div style="position:absolute;left:60px;right:10px;top:54px;height:6px;background:#e8ecf0"></div>
      <div style="position:absolute;left:60px;right:10px;top:66px;height:6px;background:#e8ecf0"></div>
      <div style="position:absolute;left:60px;right:10px;top:78px;height:6px;background:#e8ecf0"></div>
      <div style="position:absolute;left:60px;right:10px;top:90px;height:6px;background:#e8ecf0"></div>
    </div>
    <div class="foot"></div>
  </section>

  <!-- Row 7 -->
  <section class="slide col-l r7">
    <div class="brand" style="right:18px;top:14px"><span class="dot"></span>KESTREL GROUP</div>
    <div class="abs" style="left:24px;top:24px"><div class="kicker">Development</div><div class="title">Of Business</div></div>
    <div class="abs" style="left:24px;top:72px;width:180px;height:150px;border:1px solid var(--orange);padding:10px">
      <p class="body">Build a steady pipeline by setting weekly call goals, asking for referrals and following up with past clients. Track results and adjust your plan each month to keep growth on course.</p>
    </div>
    <svg class="abs" style="left:225px;top:40px" width="280" height="190" viewBox="0 0 280 190" role="img" aria-label="Bar chart of yearly placements by quarter">
      <text x="140" y="12" text-anchor="middle" font-family="Montserrat" font-weight="600" font-size="8" fill="#2e3d50">Year Over Year Growth</text>
      <g stroke="#e4e7eb"><line x1="20" y1="40" x2="270" y2="40"/><line x1="20" y1="80" x2="270" y2="80"/><line x1="20" y1="120" x2="270" y2="120"/><line x1="20" y1="160" x2="270" y2="160"/></g>
      <g>
        <rect x="40" y="110" width="12" height="50" fill="#2e3d50"/><rect x="54" y="95" width="12" height="65" fill="#F0912C"/><rect x="68" y="120" width="12" height="40" fill="#aab2bc"/>
        <rect x="100" y="90" width="12" height="70" fill="#2e3d50"/><rect x="114" y="75" width="12" height="85" fill="#F0912C"/><rect x="128" y="105" width="12" height="55" fill="#aab2bc"/>
        <rect x="160" y="70" width="12" height="90" fill="#2e3d50"/><rect x="174" y="55" width="12" height="105" fill="#F0912C"/><rect x="188" y="95" width="12" height="65" fill="#aab2bc"/>
        <rect x="220" y="50" width="12" height="110" fill="#2e3d50"/><rect x="234" y="35" width="12" height="125" fill="#F0912C"/><rect x="248" y="80" width="12" height="80" fill="#aab2bc"/>
      </g>
      <g font-family="Open Sans" font-size="7" fill="#7d8590" text-anchor="middle">
        <text x="60" y="174">Q1</text><text x="120" y="174">Q2</text><text x="180" y="174">Q3</text><text x="240" y="174">Q4</text>
      </g>
    </svg>
    <div class="foot"></div>
  </section>

  <section class="slide col-r r7" style="background:var(--navy)">
    <div class="photo cool" style="left:200px;top:0;width:325px;height:249px;clip-path:polygon(20% 0,100% 0,100% 100%,0 100%)" role="img" aria-label="Photo of a presenter speaking to a seated team"></div>
    <svg class="abs" style="left:0;top:0" width="525" height="255"><polygon points="200,249 265,0 277,0 212,249" fill="#F0912C"/></svg>
    <div class="brand light" style="left:40px;top:110px;font-size:9px"><span class="dot" style="width:14px;height:14px"></span>KESTREL GROUP</div>
    <div class="foot" style="background:var(--orange)"></div>
  </section>

</div>
</body>
</html>
```